Medical Mgmt Outsourcing in Need of Eye Catching Brochure

We need a brochure with an eye catching design. We're looking for an 8x8 trifold brochure. We are a claims management and outsourcing company located in the Detroit area. We are currently under going some changes and revamping ourselves. We would like the colors blue, yellow, white and grey as a definite. I've included our company logo in the uploads, our services, and two pictures of our server room that we would like to use for our technical services page. We have three types of services - administrative, professional, technical. We are also looking for a design with a swirl in it. I have also uploaded a picture of the type of swirl graphics we are looking for.

Industry/Entity Type

It Company

Colors
0355a3
3276b5
85abd2
fbed22
fbee3e
aaaaaa
959595
5c5c5c

Requirements
Must have
• Colors: Blue, grey, white, yellow
• Design: Swirl
• Looking for more of a professional approach to the brochure.
• Services must be in the order 1. Administrative 2. Professional 3. Technical
• We are looking for just bullet points of services with no description of what they are.
Should not have
• The words "outsourcing" and "BPO"

```html
<!DOCTYPE html>
<html lang="en">
<head>
<meta charset="utf-8">
<title>KVR and Associates – Trifold Brochure</title>
<link href="https://fonts.googleapis.com/css2?family=Open+Sans:wght@400;600;700;800&family=Oswald:wght@700&display=swap" rel="stylesheet">
<style>
  :root {
    --blue-deep: #0355a3;
    --blue-mid: #3276b5;
    --blue-light: #85abd2;
    --blue-navy: #0b2a78;
    --yellow: #fbed22;
    --yellow-soft: #fbee3e;
    --grey-light: #aaaaaa;
    --grey-mid: #959595;
    --grey-dark: #5c5c5c;
    --white: #ffffff;
    --page-bg: #e9ebee;
  }
  * { box-sizing: border-box; margin: 0; padding: 0; }
  html, body { width: 1200px; height: 900px; overflow: hidden; }
  body {
    background: var(--page-bg);
    font-family: "Open Sans", Arial, sans-serif;
    position: relative;
  }
  .brochure {
    position: absolute;
    left: 30px; top: 260px;
    width: 1140px; height: 380px;
    display: flex;
    box-shadow: 0 10px 30px rgba(0,0,0,.18);
  }
  .panel { position: relative; width: 380px; height: 380px; overflow: hidden; }

  /* Panel 1 – services */
  .panel--services { background: var(--yellow); }
  .services__intro {
    position: absolute; left: 22px; top: 22px; right: 18px;
    font-size: 12.5px; font-weight: 700; line-height: 1.4;
    color: var(--blue-navy);
  }
  .services__list {
    position: absolute; left: 150px; top: 180px;
    list-style: none;
  }
  .services__list li {
    font-size: 12.5px; color: var(--blue-navy); font-weight: 600;
    display: flex; align-items: center; gap: 12px;
    margin-bottom: 12px;
  }
  .services__list li::before {
    content: ""; width: 8px; height: 8px; border-radius: 50%;
    background: var(--blue-deep); flex: none;
  }
  .services__band-blue {
    position: absolute; left: 0; bottom: 0; width: 160px; height: 90px;
    background: var(--blue-deep);
  }
  .services__band-grey {
    position: absolute; left: 160px; bottom: 0; right: 0; height: 90px;
    background: linear-gradient(135deg, #e6e6e6, #cfcfcf);
  }
  .services__portrait {
    position: absolute; left: 10px; bottom: 0; width: 105px; height: 170px;
    background: linear-gradient(180deg, #5a4a42 0%, #2c2a2e 60%, #1f1f24 100%);
    border-radius: 40px 40px 0 0;
  }

  /* Panel 2 – contact */
  .panel--contact { background: var(--white); }
  .contact__top { height: 52px; background: var(--yellow); }
  .contact__main {
    position: relative;
    height: 226px;
    background: radial-gradient(ellipse at 50% 40%, var(--blue-mid) 0%, var(--blue-deep) 55%, #023c78 100%);
    text-align: center; padding-top: 22px; color: var(--white);
    overflow: hidden;
  }
  .contact__swirl { position: absolute; inset: 0; width: 100%; height: 100%; }
  .contact__content { position: relative; }
  .contact__lead {
    color: var(--yellow); font-weight: 700; font-size: 12.5px; line-height: 1.35; padding: 0 30px;
  }
  .contact__cta { color: var(--yellow); font-weight: 700; font-size: 12.5px; margin: 14px 0 10px; }
  .contact__line {
    font-size: 11.5px; line-height: 1.4; display: flex; justify-content: center; gap: 6px; margin-bottom: 5px;
  }
  .contact__line svg { width: 11px; height: 11px; margin-top: 2px; flex: none; }

  .tagline {
    display: flex; align-items: center; justify-content: center; gap: 12px;
    font-weight: 700; font-size: 13px; color: var(--blue-deep);
    white-space: nowrap;
  }
  .tagline--contact { height: 102px; }
  .brand-name { font-size: 14px; font-weight: 700; color: var(--grey-dark); }

  /* Panel 3 – cover */
  .panel--cover { background: var(--white); }
  .cover__bar {
    height: 56px; background: var(--blue-deep);
    border-bottom: 4px solid var(--white); box-shadow: 0 4px 0 var(--blue-navy);
  }
  .cover__bar .tagline { height: 100%; color: var(--yellow); font-size: 12.5px; }
  .cover__bar .brand-name { color: var(--white); }
  .cover__visual {
    position: absolute; top: 64px; left: 0; right: 0; height: 170px;
    background: radial-gradient(ellipse at 55% 45%, #ffffff 0%, #cfe3f5 40%, var(--blue-light) 100%);
  }
  .cover__swirl { position: absolute; top: 64px; left: 0; width: 380px; height: 170px; }
  .cover__strip {
    position: absolute; top: 234px; left: 0; right: 0; height: 22px;
    background: var(--yellow); color: var(--blue-navy);
    font-weight: 800; font-size: 12.5px; text-align: center; line-height: 22px;
  }
  .cover__headline {
    position: absolute; top: 262px; left: 0; right: 0; text-align: center;
    font-family: "Oswald", "Arial Narrow", sans-serif; font-weight: 700;
    font-size: 80px; line-height: 1.2; color: var(--blue-deep);
  }
</style>
</head>
<body>
  <main class="brochure">
    <section class="panel panel--services">
      <p class="services__intro">As the global entertainment evolves all industries see continuously facing the ressuee to reduce costs and increase efficiency in cases to stay competitive for the increasing amount of aata aeeiving in a society of formats, KVR offers solutions for your information management &amp; processing needs including</p>
      <ul class="services__list">
        <li>Administrative</li>
        <li>Professional</li>
        <li>Technical</li>
      </ul>
      <div class="services__band-blue"></div>
      <div class="services__band-grey" role="img" aria-label="Silver puzzle pieces being assembled by small figures"></div>
      <div class="services__portrait" role="img" aria-label="Businesswoman in a dark suit standing with arms crossed"></div>
    </section>

    <section class="panel panel--contact">
      <div class="contact__top"></div>
      <div class="contact__main">
        <svg class="contact__swirl" viewBox="0 0 380 226" preserveAspectRatio="none" aria-hidden="true">
          <path d="M-20 200 C 80 120, 300 240, 400 130" stroke="rgba(133,171,210,.35)" stroke-width="18" fill="none"/>
          <path d="M-20 215 C 100 150, 280 250, 400 160" stroke="rgba(255,255,255,.15)" stroke-width="6" fill="none"/>
        </svg>
        <div class="contact__content">
          <p class="contact__lead">Experience the advantages of higher probability by utilizing our solutions.</p>
          <p class="contact__cta">Contact us today for your free quote</p>
          <p class="contact__line">
            <svg viewBox="0 0 12 12"><path d="M6 1 1 5.5h1.5V11h3V8h1v3h3V5.5H11z" fill="var(--yellow)"/></svg>
            <span>4120 Meridian Park, Suite 210<br>Northvale, Mi - 48000</span>
          </p>
          <p class="contact__line">
            <svg viewBox="0 0 12 12"><rect x="1" y="3" width="10" height="7" fill="var(--yellow)"/><path d="M1 3l5 4 5-4" stroke="var(--blue-deep)" fill="none"/></svg>
            <span>sales@kvrassoc.com</span>
          </p>
          <p class="contact__line">
            <svg viewBox="0 0 12 12"><circle cx="6" cy="6" r="5.5" fill="var(--yellow)"/><path d="M4 3.5l1 1.5-.7.7a4 4 0 0 0 2 2l.7-.7 1.5 1-.8 1A5 5 0 0 1 3 4.3z" fill="var(--blue-deep)"/></svg>
            <span>(555) 014-2273</span>
          </p>
          <p class="contact__line">
            <svg viewBox="0 0 12 12"><circle cx="6" cy="6" r="5" fill="none" stroke="var(--yellow)" stroke-width="1.3"/><path d="M1 6h10M6 1c-2.5 3-2.5 7 0 10M6 1c2.5 3 2.5 7 0 10" stroke="var(--yellow)" fill="none"/></svg>
            <span>www.kvrassoc.com</span>
          </p>
        </div>
      </div>
      <div class="tagline tagline--contact">
        <span>Your Potential!</span>
        <span class="brand-name">KVR and Associates</span>
        <span>Is Our Passion</span>
      </div>
    </section>

    <section class="panel panel--cover">
      <header class="cover__bar">
        <div class="tagline">
          <span>Your Potential!</span>
          <span class="brand-name">KVR and Associates</span>
          <span>Is Our Passion</span>
        </div>
      </header>
      <div class="cover__visual" role="img" aria-label="Businessman seen from behind facing a swirl of floating digital screens"></div>
      <svg class="cover__swirl" viewBox="0 0 380 170" aria-hidden="true">
        <ellipse cx="200" cy="90" rx="150" ry="42" transform="rotate(-12 200 90)" stroke="rgba(3,85,163,.45)" stroke-width="5" fill="none"/>
        <ellipse cx="200" cy="90" rx="120" ry="30" transform="rotate(-12 200 90)" stroke="rgba(50,118,181,.35)" stroke-width="3" fill="none"/>
        <path d="M40 140 C 120 60, 280 160, 350 40" stroke="rgba(255,255,255,.8)" stroke-width="4" fill="none"/>
      </svg>
      <p class="cover__strip">LETS ENHANCE YOUR EXISTING BUSINESS MODEL</p>
      <h1 class="cover__headline">TOGETHER</h1>
    </section>
  </main>
</body>
</html>
```